PLOV Crossway Summit Poster

We are a cellular therapy (bone marrow transplants, etc) accreditation foundation who needs a poster design for a small workshop that we are going to host within a large workshop. The workshop will 1) Educate doctors who inspect program trying to get accredited. 2) Educate programs on how to become accredited.

It will be printed and mounted on foam board for display at the PLOV booth in exhibition halls. Dimensions should be 11 x 17 inches.

Our website is www.plovsite-example.org. The design does not have to have the same theme/colors as our website.

The poster should have written:

Cellular Therapy Inspection and Accreditation Workshop
February 10th, 2015
Orvell Crossway Summit
San Diego, CA

The statement below should be in small, subtle text to allow room for the other information. All returns, italics, and trademark symbols must be used exactly as included below:

The Halvering Institute of Health Sciences, Office for Ongoing Learning is accredited by the Certification Board for Ongoing Clinical Training to provide continuing medical education for physicians.

The Halvering Institute of Health Sciences, Office for Ongoing Learning designates this live activity for a maximum of 7.5 QLB VRX Tier 1 Unit(s)™. Physicians should claim only credit commensurate with the extent of their participation in the activity.

It should also have our logo on it (I have attached 2, use the one that has the best resolution)

Let me know if there are any questions!

```html
<!DOCTYPE html>
<html lang="en">
<head>
<meta charset="utf-8">
<title>PLOV Crossway Summit Poster</title>
<link rel="stylesheet" href="https://fonts.googleapis.com/css2?family=Exo+2:wght@600;700&family=Arimo:wght@400;700&family=Bitter:wght@800&display=swap">
<style>
  :root {
    --page-bg: #e9e6e1;
    --frame-blue: #1d5a7e;
    --title-blue: #1a7ab5;
    --brand-red: #e3232c;
    --logo-band: #e4e4e4;
    --white: #ffffff;
    --note-blue: #1d4f78;
    --label-grey: rgba(95, 100, 104, 0.82);
  }
  * { box-sizing: border-box; margin: 0; padding: 0; }
  html, body { width: 1000px; height: 1200px; overflow: hidden; }
  body { background: var(--page-bg); position: relative; }

  .poster {
    position: absolute; left: 131px; top: 30px;
    width: 737px; height: 1140px;
    background: var(--frame-blue);
    padding: 14px;
    display: flex; flex-direction: column;
  }
  .top-strip { height: 14px; background: var(--white); }
  .logo-band {
    height: 157px; background: var(--logo-band);
    display: flex; align-items: center; justify-content: center; gap: 18px;
  }
  .logo-square { width: 26px; height: 26px; background: var(--brand-red); }
  .logo-name {
    font-family: "Exo 2", sans-serif; font-weight: 600;
    font-size: 84px; color: var(--brand-red); letter-spacing: 4px; line-height: 1;
  }
  .title-band {
    height: 120px; background: var(--white);
    display: flex; align-items: center; justify-content: center;
  }
  .workshop-title {
    font-family: "Exo 2", sans-serif; font-weight: 700;
    font-size: 34px; line-height: 1.38; color: var(--title-blue);
    text-align: center;
  }
  .gap-top { height: 16px; }
  .hero {
    height: 536px; position: relative;
    background: linear-gradient(180deg, #3f78ad 0%, #6d9ccb 40%, #a9c6e0 66%, #8fb0c8 69%, #3f7196 74%, #24557a 88%, #1c4564 100%);
  }
  .city-label {
    position: absolute; right: 0; bottom: 26px;
    width: 296px; height: 67px; background: var(--label-grey);
    display: flex; align-items: center; justify-content: center;
    font-family: "Exo 2", sans-serif; font-weight: 700; font-size: 31px; color: var(--white);
  }
  .gap-bottom { height: 17px; }
  .info {
    flex: 1; background: var(--white);
    display: flex; flex-direction: column; align-items: stretch;
    padding-top: 40px;
  }
  .accreditation-band {
    height: 49px;
    background: linear-gradient(90deg, #1d5a7e 0%, #2e6b8f 55%, #7fa3bb 85%, #c9d8e2 100%);
    display: flex; align-items: center; justify-content: center;
    padding: 0 18px;
    font-family: "Arimo", sans-serif; font-weight: 700; font-size: 11.2px; line-height: 1.3;
    color: var(--white); text-align: center;
  }
  .credit-note {
    padding: 10px 22px 0;
    font-family: "Arimo", sans-serif; font-size: 10.6px; line-height: 1.25;
    color: var(--note-blue); text-align: center;
  }
  .event-band {
    margin-top: 9px; height: 67px;
    background: linear-gradient(90deg, #ffffff 0%, #5b8aa6 22%, #1d5a7e 50%, #5b8aa6 78%, #ffffff 100%);
    display: flex; flex-direction: column; align-items: center; justify-content: center;
    font-family: "Bitter", serif; font-weight: 800; font-size: 20px; line-height: 1.3;
    color: var(--white); letter-spacing: 0.5px;
  }
</style>
</head>
<body>
  <main class="poster">
    <div class="top-strip"></div>
    <header class="logo-band">
      <span class="logo-square"></span>
      <span class="logo-name">PLOV</span>
    </header>
    <section class="title-band">
      <h1 class="workshop-title">Cellular Therapy Inspection and<br>Accreditation Workshop</h1>
    </section>
    <div class="gap-top"></div>
    <section class="hero" role="img" aria-label="Photograph of a long curved bridge over San Diego Bay with a sailboat on sunlit water">
      <div class="city-label">San Diego</div>
    </section>
    <div class="gap-bottom"></div>
    <section class="info">
      <p class="accreditation-band">The Halvering Institute of Health Sciences, Office for Ongoing Learning is accredited by the Certification Board for Ongoing Clinical Training to provide continuing medical education for physicians.</p>
      <p class="credit-note">The Halvering Institute of Health Sciences, Office for Ongoing Learning designates this live activity for a maximum of 7.5 QLB VRX Tier 1 Unit(s)™. Physicians should claim only credit commensurate with the extent of their participation in the activity.</p>
      <div class="event-band">
        <span>February 10th, 2015</span>
        <span>Orvell Crossway Summit San Diego, CA</span>
      </div>
    </section>
  </main>
</body>
</html>
```